Craft Beer Needs a Label/ Logo Design

Name: Lanternfall
(Lanternfall Ale, Lanternfall Pilsner, Lanternfall Stout)

We are looking for a logo-ed label that will resonate domestically and internationally for this new Craft Beer Brand.

Target Market(s)

Millenials

Logo Text

Lanternfall Pilsner

Logo styles of interest
Emblem Logo
Character Logo
Colors

Designer to choose colors to be used in the design.

Requirements
Must have
• A labled logo design -- "Lanternfall" is the name, but would like to see samples with "Ale", "Pilsner", or "Stout" after!

```html
<!DOCTYPE html>
<html lang="en">
<head>
<meta charset="UTF-8">
<title>Lanternfall Craft Beer Labels</title>
<link rel="stylesheet" href="https://fonts.googleapis.com/css2?family=Libre+Baskerville:wght@400;700&display=swap">
<style>
  :root {
    --paper: #ffffff;
    --ink: #1c1c1c;
    --label-dark: #1b1b1b;
    --label-text: #f2f2f2;
    --pilsner-sky: #2b2b2b;
    --ale-sky: #6a5148;
    --stout-sky: #cbb68f;
  }
  html, body {
    margin: 0;
    padding: 0;
    width: 1200px;
    height: 858px;
    overflow: hidden;
    background: var(--paper);
  }
  .canvas {
    position: relative;
    width: 1200px;
    height: 858px;
    background: var(--paper);
    font-family: "Libre Baskerville", "Baskerville", Georgia, serif;
  }
  .label {
    position: absolute;
    display: block;
  }
  .label--pilsner { left: 68px; top: 68px; }
  .label--ale { left: 68px; top: 304px; }
  .label--stout { left: 68px; top: 566px; }
  .label--feature { left: 549px; top: 150px; }

  .label__brand {
    font-family: "Libre Baskerville", Georgia, serif;
    font-weight: 700;
    font-size: 14px;
    fill: var(--label-text);
  }
  .label__style {
    font-family: "Libre Baskerville", Georgia, serif;
    font-weight: 700;
    font-size: 16px;
    letter-spacing: 0.5px;
    fill: var(--label-text);
  }
  .label__abv {
    font-family: "Libre Baskerville", Georgia, serif;
    font-weight: 700;
    font-size: 6.5px;
    fill: var(--label-text);
  }
  .label__rule { fill: var(--label-text); }
  .label__band { fill: var(--label-dark); }

  .wordmark {
    position: absolute;
    left: 515px;
    top: 620px;
    display: flex;
    align-items: center;
    gap: 22px;
  }
  .wordmark__dot {
    width: 58px;
    height: 58px;
    border-radius: 50%;
    background: var(--ink);
  }
  .wordmark__name {
    margin: 0;
    font-family: "Libre Baskerville", Georgia, serif;
    font-weight: 700;
    font-size: 80px;
    line-height: 1;
    color: var(--ink);
  }
</style>
</head>
<body>
<main class="canvas">

  <!-- Pilsner label -->
  <svg class="label label--pilsner" width="280" height="204" viewBox="0 0 280 204" aria-labelledby="pilsner-title">
    <title id="pilsner-title">Lanternfall Pilsner label</title>
    <defs>
      <clipPath id="pilsner-shape">
        <rect x="0" y="36" width="280" height="126"/>
        <circle cx="140" cy="58" r="58"/>
        <circle cx="140" cy="144" r="58"/>
      </clipPath>
      <radialGradient id="pilsner-glow" cx="0.5" cy="0.5" r="0.5">
        <stop offset="0" stop-color="#d8d8d8" stop-opacity="0.7"/>
        <stop offset="1" stop-color="#d8d8d8" stop-opacity="0"/>
      </radialGradient>
    </defs>
    <g clip-path="url(#pilsner-shape)">
      <g role="img" aria-label="Night sky with clouds and a full moon">
        <rect x="0" y="0" width="280" height="204" fill="var(--pilsner-sky)"/>
        <circle cx="200" cy="56" r="36" fill="url(#pilsner-glow)"/>
      </g>
      <path class="label__band" d="M0 180 q8 -20 35 -17.5 t35 -17.5 t35 -17.5 t35 -17.5 t35 -17.5 t35 -17.5 t35 -17.5 t35 -17.5 L280 204 L0 204 Z" opacity="0.55"/>
    </g>
    <text class="label__brand" x="140" y="63" text-anchor="middle">Lanternfall</text>
    <rect class="label__rule" x="135" y="132" width="10" height="1.6"/>
    <text class="label__style" x="140" y="152" text-anchor="middle">PILSNER</text>
    <rect class="label__rule" x="135" y="157" width="10" height="1.6"/>
    <text class="label__abv" x="140" y="180" text-anchor="middle">4% VOL</text>
  </svg>

  <!-- Ale label -->
  <svg class="label label--ale" width="280" height="204" viewBox="0 0 280 204" aria-labelledby="ale-title">
    <title id="ale-title">Lanternfall Ale label</title>
    <defs>
      <clipPath id="ale-shape">
        <rect x="0" y="36" width="280" height="126"/>
        <circle cx="140" cy="58" r="58"/>
        <circle cx="140" cy="144" r="58"/>
      </clipPath>
      <radialGradient id="ale-glow" cx="0.5" cy="0.5" r="0.5">
        <stop offset="0" stop-color="#e6dcd6" stop-opacity="0.75"/>
        <stop offset="1" stop-color="#e6dcd6" stop-opacity="0"/>
      </radialGradient>
    </defs>
    <g clip-path="url(#ale-shape)">
      <g role="img" aria-label="Brown night sky with clouds and a full moon">
        <rect x="0" y="0" width="280" height="204" fill="var(--ale-sky)"/>
        <circle cx="200" cy="56" r="36" fill="url(#ale-glow)"/>
      </g>
      <path class="label__band" d="M0 170 q8 -20 35 -17.5 t35 -17.5 t35 -17.5 t35 -17.5 t35 -17.5 t35 -17.5 t35 -17.5 t35 -17.5 L280 204 L0 204 Z"/>
    </g>
    <text class="label__brand" x="140" y="63" text-anchor="middle">Lanternfall</text>
    <rect class="label__rule" x="135" y="124" width="10" height="1.6"/>
    <text class="label__style" x="140" y="144" text-anchor="middle">ALE</text>
    <rect class="label__rule" x="135" y="149" width="10" height="1.6"/>
    <text class="label__abv" x="140" y="178" text-anchor="middle">4% VOL</text>
  </svg>

  <!-- Stout label -->
  <svg class="label label--stout" width="280" height="204" viewBox="0 0 280 204" aria-labelledby="stout-title">
    <title id="stout-title">Lanternfall Stout label</title>
    <defs>
      <clipPath id="stout-shape">
        <rect x="0" y="36" width="280" height="126"/>
        <circle cx="140" cy="58" r="58"/>
        <circle cx="140" cy="144" r="58"/>
      </clipPath>
      <radialGradient id="stout-glow" cx="0.5" cy="0.5" r="0.5">
        <stop offset="0" stop-color="#f3ecdf" stop-opacity="0.75"/>
        <stop offset="1" stop-color="#f3ecdf" stop-opacity="0"/>
      </radialGradient>
    </defs>
    <g clip-path="url(#stout-shape)">
      <g role="img" aria-label="Golden night sky with clouds and a full moon">
        <rect x="0" y="0" width="280" height="204" fill="var(--stout-sky)"/>
        <circle cx="200" cy="56" r="36" fill="url(#stout-glow)"/>
      </g>
      <path class="label__band" d="M0 172 q8 -20 35 -17.5 t35 -17.5 t35 -17.5 t35 -17.5 t35 -17.5 t35 -17.5 t35 -17.5 t35 -17.5 L280 204 L0 204 Z"/>
    </g>
    <text class="label__brand" x="140" y="63" text-anchor="middle">Lanternfall</text>
    <rect class="label__rule" x="135" y="124" width="10" height="1.6"/>
    <text class="label__style" x="140" y="148" text-anchor="middle">STOUT</text>
    <rect class="label__rule" x="135" y="153" width="10" height="1.6"/>
    <text class="label__abv" x="140" y="178" text-anchor="middle">4% VOL</text>
  </svg>

  <!-- Featured Ale label, shown flat -->
  <svg class="label label--feature" width="392" height="286" viewBox="0 0 280 204" aria-labelledby="feature-title">
    <title id="feature-title">Lanternfall Ale label, featured</title>
    <defs>
      <clipPath id="feature-shape">
        <rect x="0" y="36" width="280" height="126"/>
        <circle cx="140" cy="58" r="58"/>
        <circle cx="140" cy="144" r="58"/>
      </clipPath>
      <radialGradient id="feature-glow" cx="0.5" cy="0.5" r="0.5">
        <stop offset="0" stop-color="#e6dcd6" stop-opacity="0.75"/>
        <stop offset="1" stop-color="#e6dcd6" stop-opacity="0"/>
      </radialGradient>
    </defs>
    <g clip-path="url(#feature-shape)">
      <g role="img" aria-label="Brown night sky with clouds and a full moon">
        <rect x="0" y="0" width="280" height="204" fill="var(--ale-sky)"/>
        <circle cx="200" cy="56" r="36" fill="url(#feature-glow)"/>
      </g>
      <path class="label__band" d="M0 170 q8 -20 35 -17.5 t35 -17.5 t35 -17.5 t35 -17.5 t35 -17.5 t35 -17.5 t35 -17.5 t35 -17.5 L280 204 L0 204 Z"/>
    </g>
    <text class="label__brand" x="140" y="63" text-anchor="middle">Lanternfall</text>
    <rect class="label__rule" x="135" y="124" width="10" height="1.6"/>
    <text class="label__style" x="140" y="144" text-anchor="middle">ALE</text>
    <rect class="label__rule" x="135" y="149" width="10" height="1.6"/>
    <text class="label__abv" x="140" y="178" text-anchor="middle">4% VOL</text>
  </svg>

  <!-- Brand wordmark -->
  <div class="wordmark">
    <span class="wordmark__dot" aria-hidden="true"></span>
    <h1 class="wordmark__name">Lanternfall</h1>
  </div>

</main>
</body>
</html>
```